Business Card design which attached logo. Company is called Tailored Shield and main colours are Orange & Black.

Company specialises in Paint Protection and Detailing for supercars.

Details needed on business card:

Sales

Address: Unit 14, 227 Harlow Street, Fernmere Vale, NSW 2391

Phone: 02 8419 2753

website: www.tailoredshield.com.au

Email: sales@tailoredshield.com.au

```html
<!DOCTYPE html>
<html lang="en">
<head>
<meta charset="utf-8">
<title>Tailored Shield – Business Card</title>
<link rel="stylesheet" href="https://fonts.googleapis.com/css2?family=Arimo:wght@400&family=Source+Sans+3:wght@500&display=swap">
<style>
  :root {
    --page: #e8e5e0;
    --card-top: #2b2b2b;
    --card-bottom: #111111;
    --orange: #f26522;
    --amber: #f7941d;
    --ink: #111111;
  }
  * { margin: 0; padding: 0; box-sizing: border-box; }
  html, body { width: 1200px; height: 1200px; overflow: hidden; }
  body {
    background: var(--page);
    position: relative;
    font-family: "Arimo", Arial, sans-serif;
  }
  .card {
    position: absolute;
    left: 210px;
    width: 780px;
    height: 444px;
    background: linear-gradient(180deg, var(--card-top), var(--card-bottom));
    box-shadow: 0 4px 14px rgba(0,0,0,0.35);
    overflow: hidden;
  }
  .card--front { top: 140px; }
  .card--back { top: 650px; }
  .card__wave { position: absolute; left: 0; top: 0; width: 780px; height: 444px; }
  .card__website {
    position: absolute;
    right: 29px;
    bottom: 18px;
    font-family: "Source Sans 3", "Myriad Pro", sans-serif;
    font-weight: 500;
    font-size: 22px;
    color: var(--ink);
    letter-spacing: 0.2px;
  }
  .brand-name {
    position: absolute;
    left: 0;
    right: 0;
    top: 140px;
    text-align: center;
    font-family: "Arimo", Arial, sans-serif;
    font-weight: 400;
    font-size: 34px;
    color: var(--orange);
  }
  .department {
    position: absolute;
    left: 74px;
    width: 281px;
    top: 140px;
    text-align: center;
    font-size: 48px;
    font-weight: 400;
    color: var(--amber);
    padding-bottom: 10px;
    border-bottom: 2px solid var(--amber);
  }
  .contact {
    position: absolute;
    left: 408px;
    top: 86px;
    list-style: none;
  }
  .contact__item {
    display: flex;
    align-items: flex-start;
    gap: 12px;
    font-size: 21px;
    line-height: 27px;
    color: var(--orange);
  }
  .contact__item + .contact__item { margin-top: 38px; }
  .contact__icon { width: 26px; height: 26px; flex: none; fill: var(--amber); }
</style>
</head>
<body>
  <svg width="0" height="0" style="position:absolute">
    <defs>
      <linearGradient id="band-light" x1="0" x2="1" y1="0" y2="0">
        <stop offset="0" stop-color="#ffdb2f"/>
        <stop offset="0.5" stop-color="#ffb300"/>
        <stop offset="1" stop-color="#ff8a00"/>
      </linearGradient>
      <linearGradient id="band-deep" x1="0" x2="1" y1="0" y2="0">
        <stop offset="0" stop-color="#ffb000"/>
        <stop offset="0.55" stop-color="#ff8c00"/>
        <stop offset="1" stop-color="#ff6000"/>
      </linearGradient>
      <symbol id="wave" viewBox="0 0 780 444">
        <path d="M0 312 C120 345 220 360 320 342 S620 280 780 292 L780 444 L0 444Z" fill="url(#band-light)"/>
        <path d="M0 375 C110 400 230 402 340 372 S620 300 780 302 L780 444 L0 444Z" fill="url(#band-deep)"/>
      </symbol>
    </defs>
  </svg>

  <section class="card card--front">
    <svg class="card__wave" viewBox="0 0 780 444"><use href="#wave"/></svg>
    <p class="brand-name">Tailored Shield</p>
    <p class="card__website">www.tailoredshield.com.au</p>
  </section>

  <section class="card card--back">
    <svg class="card__wave" viewBox="0 0 780 444"><use href="#wave"/></svg>
    <h2 class="department">SALES</h2>
    <ul class="contact">
      <li class="contact__item">
        <svg class="contact__icon" viewBox="0 0 24 24"><path d="M1 5h22v14H1z"/><path d="M2 6l10 7 10-7" fill="none" stroke="#1b1b1b" stroke-width="1.4"/></svg>
        <span>sales@tailoredshield.com.au</span>
      </li>
      <li class="contact__item">
        <svg class="contact__icon" viewBox="0 0 24 24"><path d="M6.6 2.5l3 3.6-1.8 2.4c1.2 2.6 3.2 4.6 5.7 5.8l2.4-1.8 3.6 3-1.7 3.4C10.6 18.6 5.4 13.4 3.2 5.9z"/></svg>
        <span>02 8419 2753</span>
      </li>
      <li class="contact__item">
        <svg class="contact__icon" viewBox="0 0 24 24"><path d="M12 2 1 12h3v10h6v-6h4v6h6V12h3z"/></svg>
        <span>Unit 14, 227 Harlow Street,<br>Fernmere Vale, NSW 2391</span>
      </li>
    </ul>
    <p class="card__website">www.tailoredshield.com.au</p>
  </section>
</body>
</html>
```